Cognitive therapist.

I am a therapist and my main work is with clients who have depression and anxiety disorders.

I need something reasonably plain. Cognitive therapy is a very pragmatic approach to dealing with problems, so it isn't new agey (no offence to new age therapies at all)

Hi everyone, I am currently looking at a particular design that I will most likely go with. Cheers, Lyn

Lyn Marchet
Cognitive Therapist
BA, PG Dip Mental Health,
PG Dip Cog Beh Therapy
MKRPG

The Quillan Rooms,
Level One
47 Harwick Parade
Cnr Drayfield St & Harwick Parade
P O Box 38 215
WELLINGTON 6287

Phone: 027 463 2851 Email: lmarchet@quorvane.co.nz

www.lynmarchet.co.nz

• No illustration, or colour. not old style fonts.

```html
<!DOCTYPE html>
<html lang="en">
<head>
<meta charset="utf-8">
<title>Lyn Marchet – Business Card</title>
<link rel="stylesheet" href="https://fonts.googleapis.com/css2?family=Fira+Sans:wght@400;600&display=swap">
<style>
  :root {
    --backdrop: #eceae6;
    --blue-light: #22b2ec;
    --blue-mid: #0b93d6;
    --blue-deep: #0764ae;
    --swoosh-dark: #151515;
    --paper: #f5f4f1;
    --paper-shade: #dedcd8;
    --ink: #2a2a2a;
    --white: #ffffff;
    --icon-blue: #1b8fd0;
  }
  html, body {
    margin: 0;
    width: 1200px;
    height: 864px;
    overflow: hidden;
    background: var(--backdrop);
    font-family: "Fira Sans", Arial, sans-serif;
  }
  .card {
    position: absolute;
    left: 55px;
    top: 107px;
    width: 1090px;
    height: 650px;
    overflow: hidden;
    background: linear-gradient(100deg, var(--blue-light) 0%, var(--blue-mid) 55%, var(--blue-deep) 100%);
  }
  .card-shapes {
    position: absolute;
    inset: 0;
  }
  .portrait {
    position: absolute;
    left: 20px;
    top: 30px;
    width: 390px;
    height: 620px;
    border-radius: 170px 170px 0 0;
    background: linear-gradient(180deg, #8f8f8f 0%, #5a5a5a 55%, #3a3a3a 100%);
  }
  .identity {
    position: absolute;
    right: 20px;
    top: 34px;
    text-align: right;
    color: var(--white);
  }
  .identity .name {
    margin: 0;
    font-size: 74px;
    font-weight: 600;
    line-height: 1;
    letter-spacing: 0.5px;
    text-shadow: 0 2px 3px rgba(0,0,0,0.25);
  }
  .identity .credentials {
    margin: 14px 4px 0 0;
    font-size: 25px;
    line-height: 36px;
  }
  .contact {
    position: absolute;
    right: 14px;
    top: 326px;
    list-style: none;
    margin: 0;
    padding: 0;
    color: var(--ink);
    font-size: 26px;
  }
  .contact li {
    display: flex;
    justify-content: flex-end;
    align-items: center;
    height: 41px;
    gap: 16px;
  }
  .contact svg { width: 30px; height: 30px; }
  .address {
    position: absolute;
    right: 20px;
    top: 508px;
    margin: 0;
    text-align: right;
    color: var(--ink);
    font-size: 23px;
    line-height: 36px;
    font-style: normal;
  }
</style>
</head>
<body>
  <section class="card">
    <svg class="card-shapes" viewBox="0 0 1090 650" width="1090" height="650" aria-hidden="true">
      <defs>
        <linearGradient id="paperGrad" x1="0" y1="0" x2="0.3" y2="1">
          <stop offset="0" stop-color="var(--paper-shade)"/>
          <stop offset="0.5" stop-color="var(--paper)"/>
          <stop offset="1" stop-color="var(--white)"/>
        </linearGradient>
      </defs>
      <path d="M432 650 C432 380 700 212 1090 232 L1090 650 Z" fill="var(--swoosh-dark)"/>
      <path d="M452 650 C456 410 710 248 1090 256 L1090 650 Z" fill="var(--blue-mid)"/>
      <path d="M462 650 C468 418 716 258 1090 262 L1090 650 Z" fill="var(--white)"/>
      <path d="M478 650 C484 430 724 268 1090 270 L1090 650 Z" fill="url(#paperGrad)"/>
    </svg>

    <div class="portrait" role="img" aria-label="Black and white portrait photo of Lyn Marchet"></div>

    <header class="identity">
      <h1 class="name">Lyn Marchet</h1>
      <p class="credentials">Cognitive Therapist BA,<br>PG Dip Mental Health, PG Dip Cog Beh Therapy</p>
    </header>

    <ul class="contact">
      <li><span>027 463 2851</span>
        <svg viewBox="0 0 30 30"><circle cx="15" cy="15" r="14" fill="var(--icon-blue)"/><path d="M9 8 l4 0 l1 4 l-2 2 q2 4 5 5 l2-2 l4 1 l0 4 q-12 1-14-14z" fill="var(--white)"/></svg>
      </li>
      <li><span>lmarchet@quorvane.co.nz</span>
        <svg viewBox="0 0 30 30"><rect x="2" y="6" width="26" height="19" rx="2" fill="var(--icon-blue)"/><path d="M4 9 L15 18 L26 9" stroke="var(--white)" stroke-width="2" fill="none"/></svg>
      </li>
      <li><span>www.lynmarchet.co.nz</span>
        <svg viewBox="0 0 30 30"><circle cx="15" cy="15" r="13" fill="var(--icon-blue)"/><g stroke="var(--white)" stroke-width="1.5" fill="none"><ellipse cx="15" cy="15" rx="6" ry="13"/><line x1="2" y1="15" x2="28" y2="15"/></g></svg>
      </li>
    </ul>

    <address class="address">
      MKRPG The Quillan Rooms, Level One 47<br>
      Harwick Parade Cnr Drayfield St &amp; Harwick Parade<br>
      P O Box 38 215 WELLINGTON 6287
    </address>
  </section>
</body>
</html>
```